New Web Design Project

See attachments on the content and concept. Very important that the flow of the tiers stand out

Target Market(s)

Food and Beverage Manufacturing

Industry/Entity Type

Food and Beverage

Coding

Coded - Design and coding required

Number of Pages Required

3 page

Colors
0054AA
0677BA
7BADD7
CADEEF
E8F1F8

```html
<!DOCTYPE html>
<html lang="en">
<head>
<meta charset="utf-8">
<title>Northvale Consulting Group — SQF Consulting</title>
<link href="https://fonts.googleapis.com/css2?family=Inter:wght@400;500;600;700&family=Source+Serif+4:opsz,wght@8..60,400;8..60,600;8..60,700&display=swap" rel="stylesheet">
<style>
:root{
  --navy:#1a3768;
  --navy-deep:#163a72;
  --blue:#0054aa;
  --blue-mid:#0677ba;
  --blue-soft:#7badd7;
  --blue-pale:#cadeef;
  --blue-mist:#e8f1f8;
  --page:#f3f6fb;
  --card:#ffffff;
  --line:#dde6f1;
  --ink:#1b2233;
  --muted:#4d5870;
  --green:#2e8b3e;
  --backdrop:#b3b3b3;
}
*{box-sizing:border-box;margin:0;padding:0}
html,body{width:1200px;height:2226px;overflow:hidden}
body{background:var(--backdrop);font-family:"Inter",sans-serif;color:var(--ink);position:relative}
.page{position:absolute;left:98px;top:85px;width:1005px;height:2056px;background:var(--page)}
.wrap{position:absolute;left:136px;width:733px}
.serif{font-family:"Source Serif 4",serif}

.site-header{position:absolute;left:0;top:0;width:100%;height:45px;border-bottom:1px solid var(--line)}
.brand{position:absolute;left:136px;top:9px;display:flex;gap:8px;align-items:flex-start}
.brand-mark{width:22px;height:22px;border:1.5px solid var(--navy);border-radius:5px;margin-top:2px}
.brand-name{font-family:"Source Serif 4",serif;font-weight:700;font-size:13.5px;color:var(--navy);line-height:16px}
.brand-tag{font-size:6.5px;letter-spacing:.9px;color:var(--muted);margin-top:2px}
.nav{position:absolute;right:136px;top:8px;display:flex;align-items:center;gap:15px;font-size:8.5px;color:var(--navy);font-weight:500}
.btn{display:inline-block;border-radius:7px;font-size:8.5px;font-weight:600;padding:0 13px;line-height:26px}
.btn-primary{background:var(--navy-deep);color:#fff}
.btn-ghost{background:#fff;color:var(--ink);border:1px solid var(--line)}

.hero-copy{position:absolute;left:0;top:72px;width:375px;height:647px;background:var(--card);border:1px solid var(--line);border-radius:16px;padding:30px 27px}
.eyebrow{font-size:6.5px;font-weight:700;letter-spacing:1px;color:var(--green);text-transform:uppercase}
.hero-title{font-family:"Source Serif 4",serif;font-weight:700;font-size:40px;line-height:45px;color:var(--navy);letter-spacing:-.8px;margin-top:12px}
.hero-lead{font-size:9.5px;line-height:16px;color:var(--muted);margin-top:14px}
.hero-actions{display:flex;gap:9px;margin-top:15px}
.feature-grid{display:grid;grid-template-columns:1fr 1fr;gap:7px;margin-top:17px}
.feature{background:var(--blue-mist);border:1px solid var(--line);border-radius:8px;padding:10px 9px;font-size:7.6px;line-height:13px;color:var(--muted)}
.feature b{display:block;color:var(--navy);font-weight:600;font-size:8px}
.hero-photo{position:absolute;left:394px;top:72px;width:339px;height:647px;border-radius:16px;overflow:hidden;background:linear-gradient(170deg,#e4e9ee 0%,#b9c3cc 45%,#8f9aa4 100%)}
.photo-note{position:absolute;left:13px;right:13px;bottom:13px;background:rgba(255,255,255,.93);border-radius:10px;padding:12px 12px;font-size:7.8px;line-height:14px;color:var(--ink)}
.photo-note b{font-weight:600}

.stats{top:753px;display:grid;grid-template-columns:repeat(4,1fr);gap:9px}
.stat{background:var(--card);border:1px solid var(--line);border-radius:9px;height:66px;padding:15px 12px}
.stat strong{display:block;font-size:15.5px;font-weight:700;color:var(--blue)}
.stat span{font-size:8px;color:var(--ink);margin-top:6px;display:block}

.section-head{text-align:center}
.section-head .eyebrow{display:block}
.section-title{font-family:"Source Serif 4",serif;font-weight:700;font-size:30px;line-height:33px;color:var(--navy);margin-top:8px}
.section-lead{font-size:9px;line-height:15px;color:var(--muted);margin:10px auto 0;width:380px}

.why{top:858px}
.why-photo{position:absolute;left:0;top:137px;width:322px;height:240px;border-radius:12px;background:linear-gradient(120deg,#dfe5ea 0%,#c5ced6 50%,#5b7597 100%)}
.benefits{position:absolute;left:340px;top:146px;width:393px;list-style:none}
.benefit{position:relative;padding-left:19px;margin-bottom:16px}
.benefit svg{position:absolute;left:0;top:3px}
.benefit h3{font-family:"Source Serif 4",serif;font-weight:700;font-size:10px;color:var(--navy)}
.benefit p{font-size:7.8px;line-height:14px;color:var(--ink);margin-top:7px}

.process-band{position:absolute;left:0;top:1259px;width:100%;height:322px;background:#eef3fa;border-top:1px solid var(--line);border-bottom:1px solid var(--line)}
.process{top:1283px}
.steps{position:absolute;left:0;top:136px;width:733px;display:grid;grid-template-columns:repeat(4,1fr);gap:12px}
.step{background:var(--card);border:1px solid var(--line);border-radius:10px;height:141px;padding:20px 15px}
.step-num{font-family:"Source Serif 4",serif;font-size:20px;color:var(--blue)}
.step h3{font-family:"Source Serif 4",serif;font-weight:700;font-size:10px;color:var(--navy);margin-top:9px}
.step p{font-size:7.8px;line-height:14px;color:var(--muted);margin-top:10px}

.quote{top:1604px;height:164px;background:var(--navy-deep);border-radius:14px;text-align:center;padding:30px 40px 0;color:#fff}
.quote blockquote{font-family:"Source Serif 4",serif;font-size:23.5px;line-height:32px}
.quote cite{display:block;font-style:normal;font-size:8px;margin-top:12px}

.cta{top:1813px;height:104px;border-radius:14px;background:linear-gradient(90deg,#193e7a,#1f5199);padding:26px 20px;color:#fff}
.cta .eyebrow{color:var(--blue-pale)}
.cta h2{font-family:"Source Serif 4",serif;font-weight:700;font-size:10.5px;margin-top:9px}
.cta p{font-size:8px;margin-top:11px}
.cta .btn{position:absolute;right:20px;top:38px;background:var(--blue-pale);color:var(--navy);border-radius:8px}

.footer{top:1954px;display:flex}
.footer-brand{width:316px}
.footer-brand h2{font-family:"Source Serif 4",serif;font-weight:700;font-size:13px;color:var(--navy);margin-top:4px}
.footer-brand p{font-size:7.5px;color:var(--muted);margin-top:4px}
.footer-col{font-size:8px;color:var(--muted)}
.footer-col h3{font-family:"Source Serif 4",serif;font-weight:700;font-size:10px;color:var(--navy);margin-bottom:8px}
.footer-col li{list-style:none;margin-bottom:9px}
.footer-col.pages{width:215px}
</style>
</head>
<body>
<div class="page">
  <header class="site-header">
    <div class="brand">
      <div class="brand-mark"></div>
      <div>
        <div class="brand-name">Northvale Consulting Group</div>
        <div class="brand-tag">FOOD SAFETY &amp; SQF CERTIFICATION</div>
      </div>
    </div>
    <nav class="nav">
      <span>Home</span><span>Services</span><span>Contact</span>
      <span class="btn btn-primary">Get SQF Consultation</span>
    </nav>
  </header>

  <section class="wrap" style="top:0">
    <div class="hero-copy">
      <div class="eyebrow">SQF only • Tech driven</div>
      <h1 class="hero-title">Hire a tech-driven SQF team that helps manufacturers reach certification with confidence.</h1>
      <p class="hero-lead">Northvale Consulting Group supports food and beverage manufacturers with practical food safety systems, digital implementation, and coaching that works on the production floor — not just on audit day.</p>
      <div class="hero-actions">
        <span class="btn btn-primary">Get SQF Consultation</span>
        <span class="btn btn-ghost">Explore Services</span>
      </div>
      <div class="feature-grid">
        <div class="feature"><b>Program Design</b>HACCP plans, SOPs, forms, logs, and supporting documentation tailored to your facility.</div>
        <div class="feature"><b>Digital Build</b>Move your program into modern software like PlantTrack.io or SafeBatch.io.</div>
        <div class="feature"><b>Coaching</b>Train your team to own the system day-to-day and stay audit-ready.</div>
        <div class="feature"><b>Bilingual Support</b>Support for Spanish-speaking floor teams and documentation needs.</div>
      </div>
    </div>
    <div class="hero-photo" role="img" aria-label="Photo of a food worker in hairnet and mask inspecting products on a stainless steel conveyor line in a bright production facility">
      <div class="photo-note"><b>Built for small and mid-size manufacturers</b><br>You stay focused on production while Northvale Consulting Group brings the structure, systems, and SQF guidance.</div>
    </div>
  </section>

  <section class="wrap stats">
    <div class="stat"><strong>15+</strong><span>Clients onboarded</span></div>
    <div class="stat"><strong>100%</strong><span>SQF focused approach</span></div>
    <div class="stat"><strong>Digital</strong><span>Platform-built programs</span></div>
    <div class="stat"><strong>US</strong><span>Nationwide support</span></div>
  </section>

  <section class="wrap why">
    <div class="section-head">
      <span class="eyebrow">Why Northvale Consulting</span>
      <h2 class="section-title">Built for growing food and<br>beverage operations</h2>
      <p class="section-lead">You do not need to hire a full-time food safety director to build a credible SQF program. Northvale Consulting Group combines consulting expertise with modern implementation.</p>
    </div>
    <div class="why-photo" role="img" aria-label="Photo of a consultant holding a tablet showing a food safety checklist in a production facility"></div>
    <ul class="benefits">
      <li class="benefit"><svg width="9" height="9" viewBox="0 0 10 10"><path d="M1.5 5.2l2.3 2.3L8.5 2.5" fill="none" stroke="var(--green)" stroke-width="1.6"/></svg><h3>Lower cost than a full-time hire</h3><p>Get program design, software implementation, and coaching in one engagement.</p></li>
      <li class="benefit"><svg width="9" height="9" viewBox="0 0 10 10"><path d="M1.5 5.2l2.3 2.3L8.5 2.5" fill="none" stroke="var(--green)" stroke-width="1.6"/></svg><h3>Your program lives in software</h3><p>No more binders and scattered spreadsheets. Your SQF workflow stays organized and audit-ready.</p></li>
      <li class="benefit"><svg width="9" height="9" viewBox="0 0 10 10"><path d="M1.5 5.2l2.3 2.3L8.5 2.5" fill="none" stroke="var(--green)" stroke-width="1.6"/></svg><h3>You own it, we support it</h3><p>Your team learns how to run the system, while ongoing support remains available when needed.</p></li>
      <li class="benefit"><svg width="9" height="9" viewBox="0 0 10 10"><path d="M1.5 5.2l2.3 2.3L8.5 2.5" fill="none" stroke="var(--green)" stroke-width="1.6"/></svg><h3>Flexible, low-risk engagement</h3><p>Start with a focused project, then continue monthly if ongoing coaching makes sense.</p></li>
    </ul>
  </section>

  <div class="process-band"></div>
  <section class="wrap process">
    <div class="section-head">
      <span class="eyebrow">How it works</span>
      <h2 class="section-title">From discovery to<br>certification</h2>
      <p class="section-lead">A clear path that removes guesswork and helps your facility move toward SQF with structure.</p>
    </div>
    <div class="steps">
      <div class="step"><div class="step-num">01</div><h3>Discovery Call</h3><p>We learn about your facility, current systems, and where you are in the SQF journey.</p></div>
      <div class="step"><div class="step-num">02</div><h3>Gap Assessment</h3><p>We identify missing pieces, review priorities, and create a practical roadmap.</p></div>
      <div class="step"><div class="step-num">03</div><h3>Build &amp; Implement</h3><p>We create the program, forms, logs, and workflows directly inside your digital platform.</p></div>
      <div class="step"><div class="step-num">04</div><h3>Coach &amp; Certify</h3><p>We train your team, prepare for the audit, and support the certification process.</p></div>
    </div>
  </section>

  <section class="wrap quote">
    <blockquote>“Northvale Consulting Group did not just hand us a binder. They built our SQF system into software and coached our team until we owned it.”</blockquote>
    <cite>— SQF-Certified Manufacturing Client</cite>
  </section>

  <section class="wrap cta">
    <div class="eyebrow">Ready to talk SQF?</div>
    <h2>Need a partner who understands manufacturing realities?</h2>
    <p>Use this concept as the contest-ready homepage and connect it with the Services and Contact pages included in this package.</p>
    <span class="btn">Open Contact Page</span>
  </section>

  <footer class="wrap footer">
    <div class="footer-brand">
      <h2>Northvale Consulting Group</h2>
      <p>Tech-driven SQF consulting for food and beverage manufacturers.</p>
    </div>
    <div class="footer-col pages">
      <h3>Pages</h3>
      <ul><li>Home</li><li>Services</li><li>Contact</li></ul>
    </div>
    <div class="footer-col">
      <h3>Call to action</h3>
      <ul><li>Get SQF Consultation</li><li>View Service Details</li></ul>
    </div>
  </footer>
</div>
</body>
</html>
```